Halverns Facebook Promo

I am a singer and have a number of shows throughout 2025 that I would like to promote on Facebook, to help raise my profile and also to share on my clients social media pages. I therefore need two separate promotions suitable for Facebook : 1st - Simply As Oswin 2nd - Tam Rushko's Stay Close Tonight - All the Dorsey Kellum Classics -Each promo is to include a few logos, photo, the date and venue so that I can actively support the promotion. Please refer to the attached word document for more info.

```html
<!DOCTYPE html>
<html lang="en">
<head>
<meta charset="utf-8">
<title>Halverns Promo Banners</title>
<link rel="stylesheet" href="https://fonts.googleapis.com/css2?family=Poppins:wght@200;300;400;600;700&display=swap">
<style>
  :root {
    --board: #a5b0b2;
    --navy: #0f3249;
    --sky: #3a95c0;
    --cream: #f7ede2;
    --ink: #0f2a3d;
  }
  * { margin: 0; padding: 0; box-sizing: border-box; }
  html, body { width: 1200px; height: 1200px; overflow: hidden; }
  body { background: var(--board); font-family: "Poppins", sans-serif; position: relative; }

  .promo {
    position: absolute; left: 180px; width: 841px; height: 474px;
    display: flex; box-shadow: 0 2px 4px rgba(0,0,0,.25);
  }
  .promo--oswin { top: 102px; }
  .promo--rushko { top: 640px; }

  .promo__photo { width: 359px; height: 100%; }
  .promo--oswin .promo__photo {
    background: radial-gradient(ellipse at 55% 60%, #3f5f80 0%, #243a52 35%, #050505 70%);
  }
  .promo--rushko .promo__photo {
    background: radial-gradient(ellipse at 50% 60%, #8a8a8a 0%, #3b3b3b 35%, #0c0c12 65%),
                linear-gradient(90deg, #3a1a50, #b01e3a);
    background-blend-mode: screen;
  }

  .promo__panel { position: relative; width: 482px; height: 100%; background: var(--navy); color: var(--cream); }

  .panel__portrait {
    position: absolute; left: 70px; top: 16px; width: 332px; height: 167px;
    background: radial-gradient(ellipse at 50% 60%, #3c5f7c 0%, #1d3e57 45%, var(--navy) 75%);
  }

  .title-light {
    position: absolute; left: 0; width: 100%; top: 172px; text-align: center;
    font-weight: 200; font-size: 58px; line-height: 1; color: var(--sky); letter-spacing: -1px;
  }
  .title-bold {
    position: absolute; left: 0; width: 100%; top: 240px; text-align: center;
    font-weight: 600; font-size: 60px; line-height: 1; color: var(--cream); letter-spacing: -1px;
  }

  .presenter {
    position: absolute; left: 0; width: 100%; top: 190px; text-align: center;
    font-weight: 600; font-size: 22px; line-height: 1;
  }
  .headline {
    position: absolute; left: 0; width: 100%; top: 221px; text-align: center;
    font-weight: 600; font-size: 41px; line-height: 1; letter-spacing: -0.5px;
  }
  .subline {
    position: absolute; left: 44px; width: 408px; top: 274px; height: 28px;
    background: var(--sky); color: var(--ink); text-align: center;
    font-weight: 600; font-size: 21px; line-height: 28px;
  }

  .brand {
    position: absolute; left: 44px; width: 90px; text-align: center;
    font-weight: 600; font-size: 15px; color: var(--cream); letter-spacing: .3px;
  }
  .brand__dot { display: block; width: 26px; height: 26px; margin: 0 auto 8px; border-radius: 50%; background: var(--sky); }
  .promo--oswin .brand { top: 326px; }
  .promo--rushko .brand { top: 324px; }

  .divider { position: absolute; width: 1px; background: rgba(247,237,226,.6); }
  .promo--oswin .divider { left: 143px; top: 328px; height: 67px; }
  .promo--rushko .divider { left: 155px; top: 326px; height: 67px; }

  .event { position: absolute; }
  .promo--oswin .event { left: 158px; top: 335px; }
  .promo--rushko .event { left: 177px; top: 333px; }
  .event__date { font-weight: 700; font-size: 22px; line-height: 1.1; color: #fff; }
  .event__date em { font-style: normal; color: var(--sky); }
  .event__date sup { font-size: 11px; font-weight: 400; }
  .event__venue { font-weight: 400; font-size: 15.5px; margin-top: 6px; color: var(--cream); }

  .band { position: absolute; left: 0; bottom: 0; width: 100%; height: 51px; }
  .band--venue { background: var(--sky); }
  .band--contact { background: var(--cream); }

  .venue-pill {
    position: absolute; left: 183px; top: 408px; width: 134px; height: 27px;
    border-radius: 14px; background: var(--cream); color: var(--ink);
    text-align: center; font-weight: 600; font-size: 15px; line-height: 27px; z-index: 2;
  }
  .tagline {
    position: absolute; left: 0; width: 100%; bottom: 16px; text-align: center;
    font-size: 9.5px; color: var(--cream);
  }

  .contact-pill {
    position: absolute; left: 93px; top: 12px; width: 89px; height: 26px; border-radius: 13px;
    background: var(--sky); color: var(--cream); text-align: center; font-size: 16px; line-height: 26px;
  }
  .contact-email { position: absolute; left: 201px; top: 11px; font-size: 17px; color: var(--ink); line-height: 28px; }
</style>
</head>
<body>

<section class="promo promo--oswin">
  <div class="promo__photo" role="img" aria-label="Singer in a red beanie and embellished denim shirt holding a microphone, on black"></div>
  <div class="promo__panel">
    <div class="panel__portrait" role="img" aria-label="Portrait of the singer leaning forward with a microphone"></div>
    <div class="title-light">Simply As</div>
    <div class="title-bold">Oswin Show</div>
    <div class="brand"><span class="brand__dot"></span>HALVERNS</div>
    <div class="divider"></div>
    <div class="event">
      <p class="event__date">Monday <em>17<sup>th</sup></em> March 2025</p>
      <p class="event__venue">Halverns Hotels, Ashcombe Park</p>
    </div>
    <div class="venue-pill">Ashcombe Park</div>
    <div class="band band--venue">
      <p class="tagline">An idyllic Cotswold country escape in one of Halverns Hotels' grandest buildings.</p>
    </div>
  </div>
</section>

<section class="promo promo--rushko">
  <div class="promo__photo" role="img" aria-label="Singer in a spotted blazer performing on stage under red and blue lights"></div>
  <div class="promo__panel">
    <div class="panel__portrait" role="img" aria-label="Portrait of the singer leaning forward with a microphone"></div>
    <div class="presenter">TAM RUSHKO’S</div>
    <div class="headline">STAY CLOSE TONIGHT</div>
    <div class="subline">ALL THE DORSEY KELLUM CLASSICS</div>
    <div class="brand"><span class="brand__dot"></span>HALVERNS</div>
    <div class="divider"></div>
    <div class="event">
      <p class="event__date">Monday <em>12<sup>th</sup></em> May 2025</p>
      <p class="event__venue">Halverns Hotels, Ashcombe Park</p>
    </div>
    <div class="band band--contact">
      <div class="contact-pill">Contact:</div>
      <div class="contact-email">hello@bellmarrow.com</div>
    </div>
  </div>
</section>

</body>
</html>
```